Orva Business Card

we need a business card for flooring business called Orva Flooring, the design should be black and white. we have 2 locations

Elmsbury Showroom
527 Kellerman Road,
Elmsbury VIC 3152

Harwick Showroom
462 Bramwell Hwy,
Harwick VIC 3188

email : sales@orvaflooring.com.au
(03) 9471 2830

Please inform we sell , Laminate, Hybrid, Timber, carpet and commercial flooring

```html
<!DOCTYPE html>
<html lang="en">
<head>
<meta charset="utf-8">
<title>Orva Flooring Business Card</title>
<link href="https://fonts.googleapis.com/css2?family=Nunito+Sans:wght@300;400;700;800&display=swap" rel="stylesheet">
<style>
  :root {
    --bg: #d6d6d4;
    --card: #232323;
    --card-deep: #161616;
    --ink: #f2f2f2;
    --ink-soft: #b9b9b9;
    --ink-muted: #8a8a8a;
    --rule: #6a6a6a;
  }
  * { box-sizing: border-box; margin: 0; padding: 0; }
  html, body {
    width: 1200px; height: 1200px; overflow: hidden;
    background: var(--bg);
    font-family: "Nunito Sans", sans-serif;
  }
  .sheet {
    width: 1200px; height: 1200px;
    display: flex; flex-direction: column; align-items: center; justify-content: center;
    gap: 50px;
  }
  .card {
    width: 820px; height: 530px;
    border-radius: 34px;
    background: var(--card);
    position: relative; overflow: hidden;
    box-shadow: 0 10px 30px rgba(0,0,0,0.18);
  }

  /* Front */
  .card-front { background: var(--card-deep); }
  .front-pattern {
    position: absolute; inset: 0;
    background:
      radial-gradient(ellipse 420px 260px at 42% 42%, rgba(255,255,255,0.16), rgba(255,255,255,0) 70%),
      linear-gradient(135deg, #1a1a1a 0%, #2b2b2b 45%, #141414 100%);
  }
  .front-name {
    position: absolute; left: 600px; top: 382px;
    color: var(--ink);
    font-weight: 300; font-size: 22px; letter-spacing: 1px;
    text-align: center; line-height: 1.15;
  }

  /* Back */
  .brand-block {
    position: absolute; left: 60px; top: 140px; width: 290px;
    color: var(--ink); font-weight: 300;
    text-align: center;
  }
  .brand-name { font-size: 76px; line-height: 1; letter-spacing: 2px; }
  .brand-sub { font-size: 42px; line-height: 1.2; letter-spacing: 3px; }
  .divider {
    position: absolute; left: 368px; top: 130px;
    width: 1px; height: 190px; background: var(--rule);
  }
  .contact-list {
    position: absolute; left: 400px; top: 128px;
    list-style: none;
    display: flex; flex-direction: column; gap: 16px;
  }
  .contact-item { display: flex; align-items: flex-start; gap: 14px; color: var(--ink-soft); font-size: 15px; line-height: 1.3; }
  .contact-item strong { color: var(--ink); font-weight: 700; }
  .contact-item .strong-line { color: var(--ink); font-weight: 700; font-size: 16px; }
  .icon { width: 30px; height: 30px; flex: none; }
  .range-pill {
    position: absolute; left: 150px; right: 80px; top: 430px;
    height: 36px; border: 1px solid var(--rule); border-radius: 18px;
    display: flex; align-items: center; justify-content: center;
    color: var(--ink-soft); font-size: 14px; letter-spacing: 0.6px;
  }
  .range-pill strong { color: var(--ink); font-weight: 800; margin-right: 6px; }
</style>
</head>
<body>
<main class="sheet">

  <section class="card card-front" aria-label="Card front">
    <div class="front-pattern" role="img" aria-label="Repeating tonal Orva Flooring name pattern with a soft gloss highlight"></div>
    <div class="front-name">Orva<br>Flooring</div>
  </section>

  <section class="card card-back" aria-label="Card back">
    <div class="brand-block">
      <div class="brand-name">ORVA</div>
      <div class="brand-sub">FLOORING</div>
    </div>
    <div class="divider"></div>

    <ul class="contact-list">
      <li class="contact-item">
        <svg class="icon" viewBox="0 0 30 30"><circle cx="15" cy="15" r="14" fill="none" stroke="#6a6a6a"/><path d="M15 7a5 5 0 0 0-5 5c0 4 5 10 5 10s5-6 5-10a5 5 0 0 0-5-5z" fill="#f2f2f2"/><circle cx="15" cy="12" r="1.8" fill="#232323"/></svg>
        <span><strong>Harwick</strong> Showroom, 462 Bramwell Hwy,<br>Harwick VIC 3188</span>
      </li>
      <li class="contact-item">
        <svg class="icon" viewBox="0 0 30 30"><circle cx="15" cy="15" r="14" fill="none" stroke="#6a6a6a"/><path d="M15 7a5 5 0 0 0-5 5c0 4 5 10 5 10s5-6 5-10a5 5 0 0 0-5-5z" fill="#f2f2f2"/><circle cx="15" cy="12" r="1.8" fill="#232323"/></svg>
        <span><strong>Elmsbury</strong> Showroom, 527 Kellerman Road,<br>Elmsbury VIC 3152</span>
      </li>
      <li class="contact-item">
        <svg class="icon" viewBox="0 0 30 30"><circle cx="15" cy="15" r="14" fill="none" stroke="#6a6a6a"/><rect x="8.5" y="10" width="13" height="10" rx="1.5" fill="#f2f2f2"/><path d="M9 11l6 5 6-5" fill="none" stroke="#232323" stroke-width="1.3"/></svg>
        <span><strong>sales</strong>@orvaflooring.com.au</span>
      </li>
      <li class="contact-item">
        <svg class="icon" viewBox="0 0 30 30"><circle cx="15" cy="15" r="14" fill="none" stroke="#6a6a6a"/><path d="M11 8.5l2.5 0 1 4-1.8 1.2a9 9 0 0 0 3.6 3.6l1.2-1.8 4 1v2.5a1.5 1.5 0 0 1-1.6 1.5A12 12 0 0 1 9.5 10.1 1.5 1.5 0 0 1 11 8.5z" fill="#f2f2f2"/></svg>
        <span class="strong-line">(03) 9471 2830</span>
      </li>
    </ul>

    <div class="range-pill"><strong>WE SELL</strong> LAMINATE - HYBRID - TIMBER - CARPET &amp; COMMERCIAL FLOORING</div>
  </section>

</main>
</body>
</html>
```